Brenvick Holdings LLC, new Business cards

I'm moving offices and need new cards. Plus I'm open to modifying the current design of my card. I will keep the logo but would like to explore other layouts and fonts for the design. I've included the current double sided card for reference. I Like the navy color and white. Might be open to grays or silver. Needs to be clean and elegant.

Target Market(s)

Investors, buyers & sellers of private equities and real estate.

Contact Information for Business Card

Brenvick Holdings
Dorian P.K. Halvers, Managing Principal
418 Ostrander Ave., Suite 612
Denver, CO 80319
M: 970-555-0147, O: 303-555-0192
Dorian@brenvickholdings.example
Brenvickholdings.example

Colors
0354a2
ffffff
c4c4c4

Requirements
Must have
• Business card details.
• Logo raised or embossed, it was designed after a wax seal. Current has raised ink.
Nice to have
• Space on card to write additional notes.

```html
<!DOCTYPE html>
<html lang="en">
<head>
<meta charset="utf-8">
<title>Brenvick Holdings — Business Cards</title>
<link rel="stylesheet" href="https://fonts.googleapis.com/css2?family=Work+Sans:wght@400;600&display=swap">
<style>
  :root {
    --navy: #24205e;
    --navy-deep: #1c1850;
    --white: #ffffff;
    --silver: #c4c4c4;
    --card-gray: #c9c9c9;
    --backdrop: #8e8e8e;
  }
  * { margin: 0; padding: 0; box-sizing: border-box; }
  html, body { width: 1200px; height: 930px; overflow: hidden; }
  body {
    background: var(--backdrop);
    font-family: "Work Sans", Arial, sans-serif;
    position: relative;
  }
  .card {
    position: absolute;
    width: 560px;
    height: 320px;
    border-radius: 22px;
    overflow: hidden;
  }
  .card-back {
    left: 90px;
    top: 100px;
    background: var(--card-gray);
    display: flex;
    align-items: center;
    justify-content: center;
  }
  .card-front {
    left: 550px;
    top: 500px;
    background: var(--navy);
  }
  .card-shape { position: absolute; inset: 0; }
  .brand {
    display: flex;
    align-items: center;
    gap: 12px;
    color: var(--navy);
    font-weight: 600;
    font-size: 22px;
    letter-spacing: 0.06em;
    text-transform: uppercase;
  }
  .brand-dot {
    width: 26px;
    height: 26px;
    border-radius: 50%;
    background: var(--navy);
  }
  .card-front .brand {
    position: absolute;
    right: 40px;
    top: 70px;
  }
  .details {
    position: absolute;
    left: 40px;
    top: 150px;
    color: var(--white);
  }
  .name {
    font-weight: 600;
    font-size: 19px;
    text-transform: uppercase;
    letter-spacing: 0.01em;
  }
  .role { font-size: 13px; margin-top: 2px; }
  .address { font-size: 13px; line-height: 1.35; margin-top: 14px; }
  .contacts { list-style: none; margin-top: 12px; font-size: 13px; line-height: 1.5; }
  .contacts li { display: flex; align-items: center; gap: 9px; white-space: nowrap; }
  .contacts svg { width: 10px; height: 10px; fill: var(--white); flex: none; }
</style>
</head>
<body>
  <section class="card card-back" aria-label="Card back">
    <div class="brand"><span class="brand-dot"></span>Brenvick Holdings</div>
  </section>

  <section class="card card-front" aria-label="Card front">
    <svg class="card-shape" viewBox="0 0 560 320" preserveAspectRatio="none" aria-hidden="true">
      <path d="M112,0 Q230,232 560,212 L560,196 Q258,214 132,0 Z" fill="var(--silver)"/>
      <path d="M132,0 Q258,214 560,196 L560,0 Z" fill="var(--white)"/>
    </svg>
    <div class="brand"><span class="brand-dot"></span>Brenvick Holdings</div>
    <div class="details">
      <p class="name">Dorian P.K. Halvers</p>
      <p class="role">Managing Principal</p>
      <p class="address">418 Ostrander Ave., Suite 612<br>Denver, CO 80319</p>
      <ul class="contacts">
        <li><svg viewBox="0 0 10 10"><path d="M2,0 L4,2.5 L3,3.6 Q4.5,6 6.4,7 L7.5,6 L10,8 L8.6,10 Q3,9 0,1.4 Z"/></svg>M: 970-555-0147, O: 303-555-0192</li>
        <li><svg viewBox="0 0 10 10"><path d="M0,1.5 H10 V8.5 H0 Z M1,2.5 V7.5 H9 V2.5 L5,5.5 Z" fill-rule="evenodd"/></svg>Dorian@brenvickholdings.example</li>
        <li><svg viewBox="0 0 10 10"><circle cx="5" cy="5" r="5"/></svg>www.Brenvickholdings.example</li>
      </ul>
    </div>
  </section>
</body>
</html>
```